Recruitment of Brindle Staffing for the UK market

I want a website for the UK market to attract businesses and companies to come to us for Philipine labour. We want an information site that gives all information on what we do and how we can recruit Philippine labour.
This is a recruitment site for companies to contact us with their requirements for skilled workers coming from the Philipines over to the UK to work.

Target Market(s)

Uk Companies and businesses who want Philipine skilled workers

Industry/Entity Type

REcruitment

Coding

Coded - Design and coding required

Number of Pages Required

5+ page

Font styles to use
Sans Serif

Colors
0054AA
0677BA
7BADD7
CADEEF
E8F1F8
0094D4
00A9DD
6FCCEA
C7EBF8
E9F6FB
EE7325
F08F49
F5BC92
FAE3D3
FDF4ED
EB3D1F
EC4F4E
F09395
F8D3D4
FCEDEE

Requirements
Must have
• Look professional and corperate with drop down menus for Home ,about, services,articles. training , contact us
Nice to have
• Look at Tovel recruitment- https://tovelrecruitment.example.co.uk/. This is my current site - https://www.brindlestaffing.example.com/
Should not have
• Cartoons or silly pictures , needs to be corperate looking

```html
<!DOCTYPE html>
<html lang="en">
<head>
<meta charset="utf-8">
<title>Brindle Staffing — Skilled Philippine Workers for UK Companies</title>
<link href="https://fonts.googleapis.com/css2?family=Inter:wght@400;500;600;700;800&display=swap" rel="stylesheet">
<style>
:root{
  --red:#9b1c24;
  --red-dark:#7f141b;
  --ink:#161616;
  --muted:#6b6b6b;
  --line:#e3e3e3;
  --paper:#ffffff;
  --soft:#f4f4f4;
}
*{box-sizing:border-box;margin:0;padding:0}
html,body{width:1200px;height:2912px;overflow:hidden;background:var(--paper)}
body{font-family:"Inter",Arial,sans-serif;color:var(--ink)}
.wrap{width:1040px;margin:0 auto}
a{color:inherit;text-decoration:none}

/* header */
.site-header{height:80px;border-bottom:1px solid var(--line)}
.site-header .wrap{height:100%;display:flex;align-items:center;justify-content:space-between}
.nav{display:flex;gap:34px;font-size:12px;font-weight:600;letter-spacing:.08em;text-transform:uppercase;width:380px}
.nav.right{justify-content:flex-end}
.nav a.active{color:var(--red)}
.brand{display:flex;align-items:center;gap:10px;font-weight:800;font-size:16px;color:var(--red);text-transform:uppercase;letter-spacing:.02em}
.brand-mark{width:26px;height:26px;background:var(--red);border-radius:3px}

/* hero */
.hero{height:300px;display:flex;align-items:center}
.hero .wrap{display:flex;justify-content:space-between;align-items:flex-start}
.hero-title{border-left:5px solid var(--red);padding-left:26px;font-size:40px;line-height:1.18;font-weight:700;width:540px}
.hero-side{width:400px;padding-top:8px}
.hero-side p{font-size:14px;line-height:1.7;color:var(--muted)}
.text-link{display:inline-block;margin-top:22px;font-size:12px;font-weight:700;letter-spacing:.08em;text-transform:uppercase;color:var(--red);border-bottom:2px solid var(--red);padding-bottom:4px;float:right}

/* photo */
.hero-photo{height:420px;width:1040px;margin:0 auto;background:linear-gradient(120deg,#dfe3e6 0%,#c8ced3 45%,#2e3136 100%);position:relative}
.play{position:absolute;left:110px;top:170px}

/* cards */
.cards{height:210px;display:flex;width:1040px;margin:0 auto;gap:6px;padding-top:6px}
.card{flex:1;background:var(--red);color:#fff;padding:28px 24px}
.card h3{font-size:17px;font-weight:700;margin-bottom:12px}
.card p{font-size:12px;line-height:1.6;opacity:.85}
.card svg{margin-top:18px}

/* team */
.team{height:480px}
.team .wrap{height:100%;display:flex;align-items:center;justify-content:space-between}
.map{width:420px;height:380px;background:radial-gradient(circle at 50% 50%,#e6e6e6 0%,#f5f5f5 70%)}
.team-copy{width:470px}
.team-copy h2{font-size:34px;line-height:1.22;font-weight:700}
.team-copy h2 em{font-style:normal;color:var(--red)}
.team-copy p{font-size:14px;line-height:1.7;color:var(--muted);margin:18px 0 22px}
.team-photo{width:240px;height:110px;background:linear-gradient(135deg,#cfd5da,#8d949b)}
.team-copy .text-link{float:none}

/* stats */
.stats{height:160px;border-top:1px solid var(--line);border-bottom:1px solid var(--line)}
.stats .wrap{height:100%;display:flex}
.stat{flex:1;display:flex;align-items:center;gap:14px;padding-left:30px;border-left:1px solid var(--line)}
.stat:first-child{border-left:none;padding-left:0}
.stat strong{font-size:44px;font-weight:700}
.stat span{font-size:12px;line-height:1.4;color:var(--muted);width:80px}

/* timeline */
.timeline{height:560px}
.timeline .wrap{height:100%;display:flex;align-items:center;gap:30px}
.tl-photos{display:flex;flex-direction:column;gap:20px;width:280px}
.tl-photos div{height:200px}
.tl-photos div:first-child{background:linear-gradient(135deg,#9a8b79,#4f4a44)}
.tl-photos div:last-child{background:linear-gradient(135deg,#e6e2de,#a9b3bb)}
.tl-copy{width:330px}
.tl-copy h2{font-size:32px;font-weight:700;line-height:1.2;border-left:5px solid var(--red);padding-left:18px}
.tl-copy > p{font-size:13px;line-height:1.7;color:var(--muted);margin:18px 0}
.steps{list-style:none;border-left:2px solid var(--red);padding-left:16px}
.steps li{font-size:12px;line-height:1.6;color:var(--muted);margin-bottom:10px}
.steps b{color:var(--ink)}
.tl-big{width:370px;height:440px;background:linear-gradient(160deg,#e7e3df 0%,#c9b9a6 55%,#8a2a22 100%)}

/* blog */
.blog{height:420px}
.blog .wrap{height:100%;display:flex;align-items:center;justify-content:space-between}
.blog-head h2{font-size:36px;font-weight:700;line-height:1.18}
.btn{display:inline-block;margin-top:26px;border:1px solid var(--ink);padding:10px 20px;font-size:11px;font-weight:700;letter-spacing:.08em;text-transform:uppercase}
.posts{width:640px;display:grid;grid-template-columns:1fr 1fr;column-gap:40px;row-gap:30px}
.post{border-top:1px solid var(--line);padding-top:16px}
.post h4{font-size:15px;font-weight:600;line-height:1.4;height:42px}
.post a{display:inline-block;margin-top:12px;font-size:11px;font-weight:700;color:var(--red);letter-spacing:.05em;text-transform:uppercase}

/* footer */
.site-footer{height:282px;border-top:1px solid var(--line)}
.site-footer .wrap{padding-top:60px;display:flex;justify-content:space-between}
.footer-col{width:300px}
.footer-col h5{font-size:13px;font-weight:700;margin-bottom:14px}
.footer-col p{font-size:12px;line-height:1.8;color:var(--muted)}
.socials{display:flex;gap:10px}
.socials span{width:28px;height:28px;border-radius:50%;background:#e2e2e2}
.socials span:first-child{background:var(--red)}
.copyright{margin-top:20px;font-size:11px;color:var(--muted)}
</style>
</head>
<body>

<header class="site-header">
  <div class="wrap">
    <nav class="nav"><a class="active" href="#">Home</a><a href="#">About Us</a><a href="#">Services</a></nav>
    <a class="brand" href="#"><span class="brand-mark"></span>Brindle Staffing</a>
    <nav class="nav right"><a href="#">Articles</a><a href="#">Training</a><a href="#">Contact</a></nav>
  </div>
</header>

<section class="hero">
  <div class="wrap">
    <h1 class="hero-title">Recruiting &amp; Placing Skilled Philippine Workers into UK Companies</h1>
    <div class="hero-side">
      <p>We source skilled workers from the Philippines to work in the UK. From sourcing, vetting and visa support to arrival, we are the trusted link between quality candidates and UK businesses with a real need for dependable, trained staff.</p>
      <a class="text-link" href="#">Get in touch</a>
    </div>
  </div>
</section>

<div class="hero-photo" role="img" aria-label="Photo of a smiling professional man and a woman reviewing documents at a desk">
  <svg class="play" width="80" height="80" viewBox="0 0 80 80" aria-hidden="true"><circle cx="40" cy="40" r="40" fill="#9b1c24"/><path d="M33 27 L55 40 L33 53 Z" fill="#fff"/></svg>
</div>

<section class="cards">
  <div class="card"><h3>What We Do</h3><p>We recruit the best candidates from the Philippines for UK roles.</p><svg width="24" height="12" viewBox="0 0 24 12"><path d="M0 6h22M17 1l5 5-5 5" stroke="#fff" stroke-width="1.6" fill="none"/></svg></div>
  <div class="card"><h3>How We Help</h3><p>We save your company time and money by handling every step for you.</p><svg width="24" height="12" viewBox="0 0 24 12"><path d="M0 6h22M17 1l5 5-5 5" stroke="#fff" stroke-width="1.6" fill="none"/></svg></div>
  <div class="card"><h3>Where to Start</h3><p>Tell us what roles you need filled and we will do the rest.</p><svg width="24" height="12" viewBox="0 0 24 12"><path d="M0 6h22M17 1l5 5-5 5" stroke="#fff" stroke-width="1.6" fill="none"/></svg></div>
  <div class="card"><h3>Contact Us</h3><p>Please get in touch to start a conversation with our team today.</p><svg width="24" height="12" viewBox="0 0 24 12"><path d="M0 6h22M17 1l5 5-5 5" stroke="#fff" stroke-width="1.6" fill="none"/></svg></div>
</section>

<section class="team">
  <div class="wrap">
    <div class="map" role="img" aria-label="Map of the Philippines marking recruitment regions"></div>
    <div class="team-copy">
      <h2>We recruit the finest talent available with our dedicated <em>200</em> strong team</h2>
      <p>Our recruiters are on the ground across the islands, finding qualified people for your business.</p>
      <div class="team-photo" role="img" aria-label="Photo of recruiters meeting candidates"></div>
      <br><a class="text-link" href="#">Learn more</a>
    </div>
  </div>
</section>

<section class="stats">
  <div class="wrap">
    <div class="stat"><strong>700+</strong><span>Happy clients</span></div>
    <div class="stat"><strong>21</strong><span>Specialist recruiters</span></div>
    <div class="stat"><strong>34</strong><span>Training courses</span></div>
    <div class="stat"><strong>15+</strong><span>Years of experience</span></div>
  </div>
</section>

<section class="timeline">
  <div class="wrap">
    <div class="tl-photos">
      <div role="img" aria-label="Photo of workers in hard hats on a building site"></div>
      <div role="img" aria-label="Photo of care staff standing together"></div>
    </div>
    <div class="tl-copy">
      <h2>Recruitment Timeline</h2>
      <p>From first call to arrival, here is how we bring skilled workers from the Philippines to your business.</p>
      <ul class="steps">
        <li><b>Week 1–2:</b> We agree your roles, skills and numbers needed.</li>
        <li><b>Week 3–6:</b> Candidates are sourced, tested and interviewed.</li>
        <li><b>Week 7–12:</b> Visas, travel and training are arranged for arrival.</li>
      </ul>
    </div>
    <div class="tl-big" role="img" aria-label="Photo of a smiling nurse and a worker in a red hard hat"></div>
  </div>
</section>

<section class="blog">
  <div class="wrap">
    <div class="blog-head">
      <h2>Check Our<br>Blog Articles</h2>
      <a class="btn" href="#">See all posts</a>
    </div>
    <div class="posts">
      <div class="post"><h4>Effective Strategies for Onboarding Filipino Workers</h4><a href="#">Read more →</a></div>
      <div class="post"><h4>Unlocking Benefits of Outsourcing to the Philippines</h4><a href="#">Read more →</a></div>
      <div class="post"><h4>Why Hiring Filipino Workers Is a Smart Decision</h4><a href="#">Read more →</a></div>
      <div class="post"><h4>Filipino Workforce: Skills, Quality and Value</h4><a href="#">Read more →</a></div>
      <div class="post"><h4>Your Complete Guide to Overseas Skilled Staff</h4><a href="#">Read more →</a></div>
      <div class="post"><h4>Effective Strategies for Retaining New Employees</h4><a href="#">Read more →</a></div>
    </div>
  </div>
</section>

<footer class="site-footer">
  <div class="wrap">
    <div class="footer-col">
      <a class="brand" href="#"><span class="brand-mark"></span>Brindle Staffing</a>
      <p class="copyright">© Brindle Staffing. All rights reserved.</p>
    </div>
    <div class="footer-col">
      <h5>Contact Us</h5>
      <p>hello@brindlestaffing.example.com<br>+44 20 7946 0321<br>14 Harrow Lane, Reading, RG1 4PL<br>United Kingdom</p>
    </div>
    <div class="footer-col">
      <h5>Follow Us</h5>
      <div class="socials"><span></span><span></span><span></span><span></span></div>
    </div>
  </div>
</footer>

</body>
</html>
```